Small consulting business needs a website designed to highlight value and four offerings

My company is a dynamic consulting firm with four Core Offerings: Learning & Evaluation, Program Management, Facilitation & Coaching; Implementation & Transformation. Our mission is to facilitate organizational change and transformation, and to make space for creativity, joy, belonging, and trust. If done successfully, we grow to better understand ourselves, each other, and the work we do together.

I'd like the website to give a feeling of confidence and clarity. I want the colors to match or compliment my logo. I want to have three tabs - Our Clients, Our Services, and Government.

See attached Word document for additional content. My current website is www.BrightHarborGroup.com.

Some websites I'm inspired by:
https://www.quillmeadowworks.com
https://www.verolandpartners.com
https://tqvb.org

Some websites of people/groups in my field that I find uninspiring:
http://denisehollick.com
https://www.marrowfen.org

Target Market(s)

State and local government agencies, health tech, and corporate HR departments

Industry/Entity Type

public health, aging, government, health tech

Coding

Coded - Design and coding required

Number of Pages Required

4 page

Font styles to use
Other font styles liked:
• Calibri and Merriweather

Colors
0054AA
0677BA
7BADD7
CADEEF
E8F1F8
00AB8E
00BBA5
67D7C9
C6EFE9
E9F9F6
FFC000
F8CF3A
FAE287
FDF2CF
FEFAEE
F0912C
F2A743
F7CA91
FBE8D2
FDF5EE

Requirements
Must have
• Attached logo and content, water colors few, and photos.
Nice to have
• Real pictures, which I can provide to the chosen designer
Should not have
• AI generated characters or cartoons.

```html
<!DOCTYPE html>
<html lang="en">
<head>
<meta charset="utf-8">
<title>Bright Harbor Group</title>
<link href="https://fonts.googleapis.com/css2?family=Lora:wght@400;500;700&family=Libre+Baskerville:wght@400;700&display=swap" rel="stylesheet">
<style>
:root{
  --ink:#1d1d1b;
  --gold:#f6b619;
  --gold-line:#f0b84a;
  --orange:#f0912c;
  --teal:#00ab8e;
  --teal-soft:#c6efe9;
  --sky:#7badd7;
  --footer:#124648;
  --footer-line:#3d6f70;
  --white:#ffffff;
}
*{margin:0;padding:0;box-sizing:border-box}
html,body{width:1200px;height:4234px;overflow:hidden;background:var(--white)}
body{position:relative;font-family:"Libre Baskerville",Georgia,serif;color:var(--ink)}
.abs{position:absolute}
.serif-head{font-family:"Lora",Georgia,serif;font-weight:400}
.btn{position:absolute;display:flex;align-items:center;justify-content:center;background:var(--gold);border-radius:16px;font-size:9.5px;font-weight:700;color:var(--ink)}
.rule{display:inline-block;height:1.5px;background:var(--gold-line);vertical-align:middle}
.wash{position:absolute;pointer-events:none}

/* nav */
.brand{left:110px;top:14px;width:100px;text-align:center;font-family:"Lora",serif;font-size:11px;line-height:1.25;color:#6b5a1e}
.brand .dot{display:block;width:30px;height:30px;border-radius:50%;background:#8ab33d;margin:0 auto 6px}
.nav{left:445px;top:33px;display:flex;gap:20px;font-size:10px}
.nav-cta{left:983px;top:26px;width:94px;height:30px;font-size:9px}

/* hero */
.hero-wash{left:0;top:0;width:1200px;height:660px;
  background:
   radial-gradient(ellipse 420px 320px at 1080px 110px,#fbe79a 0%,rgba(251,231,154,0) 70%),
   radial-gradient(ellipse 480px 260px at 250px 520px,#a6dccf 0%,rgba(166,220,207,0) 72%),
   radial-gradient(ellipse 500px 300px at 750px 560px,#b9e3dc 0%,rgba(185,227,220,0) 70%),
   radial-gradient(ellipse 400px 260px at 1000px 480px,#f7e3a0 0%,rgba(247,227,160,0) 70%),
   linear-gradient(180deg,#fdfbf0 0%,#eef7ea 100%)}
.hero-kicker{left:122px;top:183px;font-size:12px}
.hero-kicker .rule{width:90px;margin-left:14px}
.hero-title{left:122px;top:205px;width:480px;font-size:42px;line-height:50px}
.hero-copy{left:122px;top:370px;width:430px;font-size:9.5px;line-height:17px}
.hero-btn{left:122px;top:447px;width:108px;height:28px}
.node-label{font-family:"Lora",serif;font-size:13px;font-weight:500;text-align:center;width:160px}

/* feature rows */
.photo-wash{border-radius:50%;filter:blur(14px)}
.photo{position:absolute;border-radius:50%}
.emblem{position:absolute;border-radius:50%;border:3px solid #1f5b5c}
.block-title{font-size:33px;line-height:40px}
.block-title .rule{width:80px;margin-left:12px}
.block-copy{font-size:10px;line-height:18.5px}
.why-copy{font-size:9.5px;line-height:17px}
.learn{width:94px;height:28px}

/* help band */
.band-title{width:1200px;text-align:center;font-size:33px}
.band-title .rule{width:80px;margin:0 16px}
.big-claim{width:1200px;text-align:center;font-family:"Lora",serif;font-weight:700;font-size:74px;line-height:100px}
.big-claim em{font-style:normal;color:var(--gold)}
.arrow{width:40px;height:40px;border:2px solid var(--gold);border-radius:50%}

/* collaborate */
.partner{position:absolute;width:140px;text-align:center;font-size:12px;line-height:18px}
.partner .ring{width:68px;height:68px;margin:0 auto 10px;border-radius:50%;border:4px solid var(--orange);box-shadow:inset 0 0 0 3px #fff,inset 0 0 0 5px #f6c67b;display:flex;align-items:center;justify-content:center}
.partner .ring span{width:30px;height:30px;border-radius:50%}

/* footer */
.footer{left:0;top:3896px;width:1200px;height:338px;background:var(--footer);color:var(--white)}
.f-head{font-family:"Lora",serif;font-size:16px}
.f-link{font-size:9px}
.social{width:24px;height:24px;border-radius:50%;border:1.5px solid var(--gold)}
.c-ico{width:22px;height:22px;border-radius:50%;border:1.5px solid var(--gold);display:flex;align-items:center;justify-content:center}
</style>
</head>
<body>

<!-- HERO -->
<div class="wash hero-wash"></div>
<svg class="abs" style="left:0;top:560px" width="1200" height="110" viewBox="0 0 1200 110" aria-hidden="true">
  <path fill="#fff" d="M0 40 L40 48 60 30 95 44 130 36 160 58 200 42 240 50 290 38 330 60 370 46 410 55 450 40 500 62 540 50 580 58 620 44 660 66 700 52 740 60 790 48 830 68 870 55 910 62 950 46 1000 58 1040 44 1080 56 1120 40 1160 52 1200 38 L1200 110 L0 110Z"/>
</svg>

<div class="abs brand"><span class="dot"></span>Bright Harbor<br>Group</div>
<nav class="abs nav"><span>Our Clients</span><span>Our Services</span><span>Government</span><span>Case Studies</span></nav>
<div class="btn nav-cta">Contact Us</div>

<p class="abs hero-kicker">Welcome to Bright Harbor Group<span class="rule"></span></p>
<h1 class="abs hero-title serif-head">A Seat at the Table for Collaboration, Learning, and Meaningful Change.</h1>
<p class="abs hero-copy">Bright Harbor Group is a dynamic consulting firm with four Core Offerings: Learning &amp; Evaluation, Program Management, Facilitation &amp; Coaching; Implementation &amp; Transformation</p>
<div class="btn hero-btn">View all Offer</div>

<svg class="abs" style="left:640px;top:100px" width="430" height="420" viewBox="640 100 430 420" aria-hidden="true">
  <circle cx="852" cy="307" r="181" fill="none" stroke="var(--gold)" stroke-width="1.5" stroke-dasharray="5 5"/>
  <g fill="#fff" stroke="var(--gold)" stroke-width="5">
    <circle cx="852" cy="127" r="22"/><circle cx="671" cy="307" r="22"/>
    <circle cx="1031" cy="307" r="22"/><circle cx="852" cy="488" r="22"/>
  </g>
  <g fill="#1f5b5c"><circle cx="852" cy="127" r="8"/><circle cx="671" cy="307" r="8"/><circle cx="1031" cy="307" r="8"/><circle cx="852" cy="488" r="8"/></g>
</svg>
<div class="photo" style="left:729px;top:184px;width:246px;height:246px;background:radial-gradient(circle at 35% 40%,#f6c02a,#6aa27a 60%,#1f5b5c);border:4px solid #1f5b5c" role="img" aria-label="Watercolor puzzle emblem of four interlocking pieces"></div>
<div class="abs node-label" style="left:772px;top:75px">Implementation</div>
<div class="abs node-label" style="left:591px;top:341px">Learning</div>
<div class="abs node-label" style="left:953px;top:341px">Facilitation</div>
<div class="abs node-label" style="left:772px;top:521px">Program Management</div>

<!-- connecting curve -->
<svg class="abs" style="left:0;top:0" width="1200" height="1400" aria-hidden="true">
  <path d="M690 850 C 600 1050, 430 1280, 258 1315" fill="none" stroke="#f3d28a" stroke-width="1.5"/>
</svg>

<!-- MISSION -->
<div class="wash photo-wash" style="left:60px;top:730px;width:470px;height:420px;background:radial-gradient(circle,#fbd9d3 0%,#fdf0cf 50%,rgba(255,255,255,0) 72%)"></div>
<div class="photo" style="left:120px;top:769px;width:346px;height:346px;background:linear-gradient(180deg,#4f8fc4 0%,#a9cde3 55%,#f2b04a 80%,#8a4a1f 100%)" role="img" aria-label="Photo of a person planting a flag on a summit at sunrise"></div>
<div class="emblem" style="left:688px;top:776px;width:124px;height:124px;background:radial-gradient(circle,#f6c02a,#6aa27a 55%,#fff 70%)" role="img" aria-label="Watercolor emblem of overlapping circles"></div>
<h2 class="abs block-title serif-head" style="left:682px;top:918px">Our Mission<span class="rule"></span></h2>
<p class="abs block-copy" style="left:682px;top:968px;width:400px">Our mission is to facilitate organizational change and transformation, and to make space for creativity, joy, belonging, and trust. If done successfully, we grow to better understand ourselves, each other, and the work we do together.</p>
<div class="btn learn" style="left:684px;top:1070px">Learn More</div>

<!-- VISION -->
<div class="emblem" style="left:124px;top:1256px;width:124px;height:124px;background:radial-gradient(circle,#f0912c,#00ab8e 50%,#fff 68%)" role="img" aria-label="Watercolor burst emblem"></div>
<h2 class="abs block-title serif-head" style="left:122px;top:1396px">Our Vision<span class="rule"></span></h2>
<p class="abs block-copy" style="left:122px;top:1446px;width:430px">Our vision is to be part of a world where organizations and collaborators connect as human beings first. We envision a future where partners and colleagues strive for ongoing growth together.</p>
<div class="btn learn" style="left:122px;top:1530px">Learn More</div>
<div class="wash photo-wash" style="left:690px;top:1190px;width:440px;height:420px;background:radial-gradient(circle,#fbd9d3 0%,#fdf0cf 50%,rgba(255,255,255,0) 72%)"></div>
<div class="photo" style="left:736px;top:1232px;width:330px;height:330px;background:radial-gradient(circle at 50% 60%,#e8c0a8 0%,#c9dbe0 50%,#9fc0cc 100%)" role="img" aria-label="Photo of open hands holding a target with an arrow in the bullseye"></div>

<!-- VALUE -->
<div class="wash photo-wash" style="left:60px;top:1710px;width:470px;height:420px;background:radial-gradient(circle,#fbd9d3 0%,#fdf0cf 50%,rgba(255,255,255,0) 72%)"></div>
<div class="photo" style="left:120px;top:1747px;width:346px;height:346px;background:linear-gradient(160deg,#5ea9d6,#7ec0e2 60%,#4b95c6)" role="img" aria-label="Photo of a hand arranging wooden blocks spelling value beside eyeglasses"></div>
<div class="emblem" style="left:673px;top:1730px;width:124px;height:124px;background:radial-gradient(circle,#f6c02a,#6aa27a 55%,#fff 70%)" role="img" aria-label="Watercolor landscape emblem with a path toward the sun"></div>
<h2 class="abs block-title serif-head" style="left:676px;top:1868px">Our Value<span class="rule"></span></h2>
<p class="abs block-copy" style="left:676px;top:1918px;width:410px">We are the tranquility in chaos. The steady partner always at the table with you. We drive meaningful and measurable change, resulting in sustained progress towards key community outcomes and multi-sector initiatives. Our work produces values realignment, critical technical assistance, and develops trategic plans for innovative organizations ready to elevate their work.</p>
<div class="btn learn" style="left:677px;top:2058px">Learn More</div>

<!-- HELP BAND -->
<div class="wash" style="left:0;top:2150px;width:1200px;height:700px;background:
  radial-gradient(ellipse 500px 260px at 200px 150px,#dbead0 0%,rgba(219,234,208,0) 70%),
  radial-gradient(ellipse 500px 250px at 1000px 130px,#e6eccd 0%,rgba(230,236,205,0) 70%),
  radial-gradient(ellipse 700px 300px at 600px 520px,#b7e1df 0%,rgba(183,225,223,0) 72%),
  linear-gradient(180deg,#eef5e6 0%,#f6f9f2 40%,#d2ece9 100%)"></div>
<svg class="abs" style="left:0;top:2140px" width="1200" height="60" viewBox="0 0 1200 60" aria-hidden="true">
  <path fill="#fff" d="M0 0 L1200 0 L1200 30 1160 22 1120 38 1080 26 1040 40 990 28 950 44 900 30 860 42 810 24 770 40 720 30 680 46 630 32 590 40 540 26 500 44 450 30 410 42 360 26 320 38 270 24 230 42 180 30 140 40 90 26 50 36 0 24Z"/>
</svg>
<svg class="abs" style="left:0;top:2790px" width="1200" height="70" viewBox="0 0 1200 70" aria-hidden="true">
  <path fill="#fff" d="M0 30 L40 20 80 36 120 18 160 34 210 22 250 40 300 26 340 38 390 20 430 36 480 24 520 42 570 28 610 40 660 22 700 38 750 26 790 44 840 28 880 38 930 20 970 36 1020 24 1060 40 1110 26 1150 36 1200 22 L1200 70 L0 70Z"/>
</svg>
<h2 class="abs band-title serif-head" style="left:0;top:2258px"><span class="rule"></span>We Help Your Team<span class="rule"></span></h2>
<div class="emblem" style="left:538px;top:2334px;width:138px;height:138px;background:radial-gradient(circle,#f6c02a,#2f8e8a 55%,#fff 70%)" role="img" aria-label="Watercolor emblem of linked figures in a circle"></div>
<p class="abs big-claim" style="left:0;top:2475px">Turn bold <em>visions</em> into<br>practical results.</p>
<svg class="abs arrow" style="left:59px;top:2499px" viewBox="0 0 40 40" aria-hidden="true"><path d="M23 12 L15 20 L23 28" fill="none" stroke="var(--gold)" stroke-width="2"/></svg>
<svg class="abs arrow" style="left:1100px;top:2499px" viewBox="0 0 40 40" aria-hidden="true"><path d="M17 12 L25 20 L17 28" fill="none" stroke="var(--gold)" stroke-width="2"/></svg>

<!-- COLLABORATE -->
<h2 class="abs band-title serif-head" style="left:0;top:2918px"><span class="rule"></span>We Collaborate With<span class="rule"></span></h2>
<p class="abs" style="left:0;top:2966px;width:1200px;text-align:center;font-size:9px">deviate more here between nonprofit and corporate</p>
<div class="partner" style="left:96px;top:3024px"><div class="ring"><span style="background:#f6c02a"></span></div>Large-scale<br>Companies</div>
<div class="partner" style="left:239px;top:3024px"><div class="ring"><span style="background:#f0912c"></span></div>National and<br>local nonprofits</div>
<div class="partner" style="left:384px;top:3024px"><div class="ring"><span style="background:#2f8e8a"></span></div>State government<br>agencies</div>
<div class="partner" style="left:527px;top:3024px"><div class="ring"><span style="background:#1f5b5c"></span></div>Foundations</div>
<div class="partner" style="left:670px;top:3024px"><div class="ring"><span style="background:#f6c02a"></span></div>Tribal Serving<br>Organizations</div>
<div class="partner" style="left:814px;top:3024px"><div class="ring"><span style="background:#f2a743"></span></div>Startups in tech</div>
<div class="partner" style="left:957px;top:3024px"><div class="ring"><span style="background:#00ab8e"></span></div>International<br>Partnerships<br>&amp; Organizations</div>

<!-- WHY US -->
<div class="wash" style="left:0;top:3180px;width:1200px;height:560px;background:
  radial-gradient(ellipse 520px 240px at 250px 330px,#fbe2a8 0%,rgba(251,226,168,0) 72%),
  radial-gradient(ellipse 520px 240px at 900px 380px,#fbdcae 0%,rgba(251,220,174,0) 72%),
  radial-gradient(ellipse 700px 180px at 600px 480px,#fdf2cf 0%,rgba(253,242,207,0) 80%)"></div>
<h2 class="abs block-title serif-head" style="left:125px;top:3300px">Why Us<span class="rule"></span></h2>
<p class="abs why-copy" style="left:122px;top:3350px;width:470px">Through our Core Offerings and guided by our founder's traditional and nontraditional methods for engaging and steering a team, we create a sense of belonging, foster transparency, and help to build stronger relationships. Our approach helps to drive meaningful change so that organizations and initiatives can clear roadblocks and meet collective goals. Our team's proven ability to transform conflict into opportunity will help to advance your organization and the communities you serve.</p>
<div class="btn learn" style="left:122px;top:3486px">Learn More</div>
<div class="emblem" style="left:756px;top:3232px;width:316px;height:316px;border-width:5px;background:linear-gradient(160deg,#4fa9a6 0%,#f6c02a 35%,#2f8e8a 60%,#e8b450 85%,#1f5b5c 100%)" role="img" aria-label="Watercolor illustration of sun over flowing waves and river stones"></div>

<!-- CTA -->
<h2 class="abs band-title serif-head" style="left:0;top:3670px;font-size:30px"><span class="rule" style="background:#7bc9bd;width:80px"></span>Ready to Accelerate Your Business Growth?<span class="rule" style="background:#7bc9bd;width:80px"></span></h2>
<p class="abs" style="left:0;top:3724px;width:1200px;text-align:center;font-size:10px">Schedule your free strategy session and discover how we can help.</p>
<div class="btn" style="left:554px;top:3765px;width:92px;height:29px;background:#fff;box-shadow:0 1px 4px rgba(0,0,0,.08)">Learn More</div>

<!-- FOOTER -->
<div class="abs footer"></div>
<svg class="abs" style="left:0;top:3860px" width="1200" height="60" viewBox="0 0 1200 60" aria-hidden="true">
  <path fill="var(--footer)" d="M0 34 L40 26 80 40 120 22 160 36 200 18 250 34 290 24 340 40 380 20 420 34 470 26 510 42 560 24 600 36 650 20 690 34 740 28 780 42 830 22 870 36 920 26 960 40 1010 20 1050 34 1100 24 1140 38 1200 26 L1200 60 L0 60Z"/>
</svg>
<div class="abs" style="left:116px;top:3966px;width:130px;text-align:center;font-family:'Lora',serif;font-size:17px;line-height:22px;color:#fff">
  <span style="display:block;width:36px;height:36px;border-radius:50%;background:#8ab33d;margin:0 auto 12px"></span>Bright Harbor<br>Group</div>

<p class="abs f-head" style="left:332px;top:3972px;color:#fff">Quick Links</p>
<p class="abs f-link" style="left:333px;top:4008px;color:#fff">Home</p>
<p class="abs f-link" style="left:333px;top:4034px;color:#fff">Our Story</p>
<p class="abs f-link" style="left:333px;top:4061px;color:#fff">Meet Our Partners</p>

<p class="abs f-head" style="left:523px;top:3972px;color:#fff">Contact Info</p>
<div class="abs c-ico" style="left:523px;top:4002px"><svg width="11" height="11" viewBox="0 0 24 24"><path d="M6 2 L10 6 8 9 C9 12 12 15 15 16 L18 14 22 18 19 22 C10 21 3 14 2 5Z" fill="var(--gold)"/></svg></div>
<p class="abs f-link" style="left:553px;top:4008px;color:#fff">+ 123 456 789</p>
<div class="abs c-ico" style="left:523px;top:4043px"><svg width="11" height="9" viewBox="0 0 22 16"><rect x="1" y="1" width="20" height="14" fill="none" stroke="var(--gold)" stroke-width="2"/><path d="M1 1 L11 9 L21 1" fill="none" stroke="var(--gold)" stroke-width="2"/></svg></div>
<p class="abs f-link" style="left:553px;top:4043px;color:#fff;line-height:13px">info@brightharbor<br>group.com</p>
<div class="abs c-ico" style="left:523px;top:4092px"><svg width="11" height="11" viewBox="0 0 24 24"><circle cx="12" cy="12" r="10" fill="none" stroke="var(--gold)" stroke-width="2"/><path d="M2 12 H22 M12 2 C6 8 6 16 12 22 M12 2 C18 8 18 16 12 22" fill="none" stroke="var(--gold)" stroke-width="2"/></svg></div>
<p class="abs f-link" style="left:553px;top:4093px;color:#fff;line-height:13px">Bright Harbor<br>group.com</p>

<p class="abs f-head" style="left:722px;top:3972px;color:#fff">Follow Us</p>
<div class="abs social" style="left:744px;top:4011px" role="img" aria-label="Social network one"></div>
<div class="abs social" style="left:744px;top:4050px" role="img" aria-label="Social network two"></div>
<div class="abs social" style="left:744px;top:4088px" role="img" aria-label="Social network three"></div>

<p class="abs f-head" style="left:858px;top:3972px;color:#fff">Newsletter Signup</p>
<div class="abs" style="left:860px;top:4011px;width:214px;height:30px;border:1px solid #fff;border-radius:15px;padding:0 14px;display:flex;align-items:center;font-size:9px;color:#fff">Email</div>
<div class="btn" style="left:860px;top:4051px;width:214px;height:30px;background:#f8cf1f;font-size:8.5px">SUBSCRIBE</div>

<div class="abs" style="left:122px;top:4160px;width:956px;height:1px;background:var(--footer-line)"></div>
<div class="abs" style="left:822px;top:4172px;width:256px;display:flex;justify-content:flex-end;gap:14px;font-size:8.5px;color:#fff"><span>Company</span><span>Privacy Policy</span><span>Terms and Conditions</span></div>

</body>
</html>
```